Flyer Design

we need a flyer design for a new company Thistlecombe Garden maintenance
we want a leaflet for our gardening services.
we do lawn cutting,hedge cutting, lawn treatments,tree work, full garden maintenance.
I have attached some ones i like so this might give you a starting point.

Industry/Entity Type

It Company

```html
<!DOCTYPE html>
<html lang="en">
<head>
<meta charset="utf-8">
<title>Thistlecombe Garden Maintenance – Flyer</title>
<link rel="stylesheet" href="https://fonts.googleapis.com/css2?family=Oswald:wght@500;600;700&family=Open+Sans:wght@700&display=swap">
<style>
  :root {
    --page-bg: #d9dbde;
    --royal-blue: #1c3fae;
    --deep-blue: #13309a;
    --pale-blue: #9aabe0;
    --panel-white: #ffffff;
    --panel-grey: #eceef1;
    --ink: #262626;
    --band-blue: rgba(170, 186, 232, 0.45);
    --band-white: rgba(255, 255, 255, 0.55);
  }
  * { margin: 0; padding: 0; box-sizing: border-box; }
  html, body {
    width: 1125px; height: 1200px; overflow: hidden;
    background: var(--page-bg);
  }
  .flyer {
    position: absolute; left: 40px; top: 231px;
    width: 1045px; height: 737px;
    overflow: hidden;
    background: var(--panel-white);
    box-shadow: 0 6px 18px rgba(0,0,0,0.18);
  }
  .flyer-shapes { position: absolute; inset: 0; width: 100%; height: 100%; }

  .brand {
    position: absolute; right: 34px; top: 128px;
    display: flex; align-items: center; gap: 12px;
    font-family: "Oswald", sans-serif; font-weight: 700;
    color: #111;
    text-transform: uppercase;
  }
  .brand-square { width: 40px; height: 40px; background: var(--royal-blue); }
  .brand-name { line-height: 1; text-align: left; }
  .brand-name .line-main { display: block; font-size: 40px; letter-spacing: 0.5px; }
  .brand-name .line-sub { display: block; font-size: 12.5px; letter-spacing: 1.4px; margin-top: 4px; }

  .services-band {
    position: absolute; left: 640px; right: 0; top: 296px; height: 58px;
    background: var(--band-blue);
  }
  .services-title {
    position: absolute; right: 34px; top: 296px; height: 58px;
    display: flex; align-items: center;
    font-family: "Oswald", sans-serif; font-weight: 600;
    font-size: 39px; color: var(--royal-blue);
    text-transform: uppercase;
  }
  .services-list {
    position: absolute; right: 34px; top: 366px;
    list-style: none; text-align: right;
    font-family: "Oswald", sans-serif; font-weight: 500;
    font-size: 31px; line-height: 52.6px;
    color: var(--ink); text-transform: uppercase;
  }

  .call-band {
    position: absolute; left: 0; width: 735px; top: 666px; height: 69px;
    background: var(--band-white);
    display: flex; align-items: center; padding-left: 56px;
    font-family: "Open Sans", sans-serif; font-weight: 700;
    font-size: 33px; color: var(--royal-blue);
  }
  .call-label { margin-right: 24px; }
  .call-icon { width: 44px; height: 44px; margin-right: 22px; }
</style>
</head>
<body>
  <article class="flyer">
    <svg class="flyer-shapes" viewBox="0 0 745 525" preserveAspectRatio="none" aria-hidden="false">
      <defs>
        <linearGradient id="gardenTones" x1="0" y1="0" x2="0" y2="1">
          <stop offset="0" stop-color="#8fc3ec"/>
          <stop offset="0.22" stop-color="#5f8a3e"/>
          <stop offset="0.45" stop-color="#8a857b"/>
          <stop offset="0.7" stop-color="#4f7d2f"/>
          <stop offset="0.86" stop-color="#6cb33a"/>
          <stop offset="1" stop-color="#5ea532"/>
        </linearGradient>
        <linearGradient id="panelTone" x1="0" y1="0" x2="1" y2="1">
          <stop offset="0" stop-color="#ffffff"/>
          <stop offset="1" stop-color="#eceef1"/>
        </linearGradient>
      </defs>

      <g role="img" aria-label="Photo of a stone cottage with a neat hedge, flower beds, lawn and a large tree under blue sky">
        <rect class="garden-photo" x="0" y="0" width="560" height="525" fill="url(#gardenTones)"/>
      </g>

      <path class="swoosh-main" fill="var(--royal-blue)"
        d="M430,0 L475,0 C445,120 455,230 508,330 C543,400 556,460 553,525 L452,525 C468,470 458,400 428,330 C398,250 400,120 430,0 Z"/>
      <path class="swoosh-pale-left" fill="var(--pale-blue)"
        d="M418,0 L436,0 C408,110 406,230 440,320 C400,240 396,110 418,0 Z"/>

      <path class="content-panel" fill="url(#panelTone)"
        d="M475,0 L745,0 L745,525 L553,525 C556,460 543,400 508,330 C455,230 445,120 475,0 Z"/>

      <path class="swoosh-pale-right" fill="var(--pale-blue)"
        d="M482,0 L548,0 C505,70 505,160 540,250 L528,250 C485,170 470,80 482,0 Z"/>
      <path class="swoosh-deep" fill="var(--deep-blue)"
        d="M548,0 L562,0 C525,70 522,150 548,235 C512,160 510,70 548,0 Z"/>
    </svg>

    <div class="brand">
      <span class="brand-square"></span>
      <span class="brand-name">
        <span class="line-main">Thistlecombe</span>
        <span class="line-sub">Garden Maintenance</span>
      </span>
    </div>

    <div class="services-band"></div>
    <h2 class="services-title">Our Services</h2>
    <ul class="services-list">
      <li>Lawn Cutting</li>
      <li>Hedge Cutting</li>
      <li>Lawn Treatments</li>
      <li>Tree Work</li>
      <li>Full Garden</li>
      <li>Maintenance</li>
    </ul>

    <div class="call-band">
      <span class="call-label">CALL NOW</span>
      <svg class="call-icon" viewBox="0 0 44 44" aria-label="Phone">
        <circle cx="22" cy="22" r="19" fill="none" stroke="var(--royal-blue)" stroke-width="3"/>
        <path fill="var(--royal-blue)"
          d="M15.5,11.5 l4,-0.5 l2.5,6 l-3,2.2 c1.3,3 3.3,5 6.3,6.3 l2.2,-3 l6,2.5 l-0.5,4 c-0.3,1.4 -1.6,2.3 -3,2.2 c-8.5,-0.8 -15.2,-7.5 -16,-16 c-0.1,-1.4 0.8,-2.7 2.2,-3 z"/>
      </svg>
      <span class="call-number">0161 555 0427</span>
    </div>
  </article>
</body>
</html>
```